Etikett für ein Erfrischungsgetränk
Zielgruppe
Veltrano ist ein Startup Unternehmen, welches in naher Zukunft ein
Hibiskus-Erfrischungsgetränk auf den Markt bringen möchte.
Die Zielgruppe ist jedermann. Ob jung oder alt.
Aufgabenstellung
Das Etikett einer 0,33 l Longneckflasche soll:
Erfrischend, Modern aber auch Zeitlos, Einzigartig, dezent wirken.
Das Logo soll hervorstehen und der Hintergrund dezent sein.
Vorderetikett: 76 mm breit, 86 mm hoch
Rücketikett: 55 mm breit, 75 mm hoch
Die Getränkfarbe ist rötlich.

```html
<!DOCTYPE html>
<html lang="de">
<head>
<meta charset="utf-8">
<title>Veltrano – Etikett</title>
<link href="https://fonts.googleapis.com/css2?family=Arimo:wght@400;700&family=Oswald:wght@500;600&display=swap" rel="stylesheet">
<style>
:root{
  --page:#efefef;
  --purple-dark:#9a1e90;
  --purple-mid:#b627a8;
  --purple-light:#c732b9;
  --frame:#cf6cc8;
  --white:#ffffff;
  --panel:#d48ec9;
  --splash-a:#eaf6fb;
  --splash-b:#7cc3df;
}
*{margin:0;padding:0;box-sizing:border-box}
html,body{width:1200px;height:900px;overflow:hidden;background:var(--page)}
.canvas{position:relative;width:1200px;height:900px;font-family:"Arimo",Arial,sans-serif;color:var(--white)}
.front-shape{position:absolute;left:0;top:0}
.brand-name{position:absolute;left:35px;width:610px;top:228px;text-align:center;font-family:"Arimo",Arial,sans-serif;font-weight:700;font-size:78px;letter-spacing:1px;color:var(--white)}
.splash{position:absolute;left:150px;top:338px;width:370px;height:330px}
.tagline{position:absolute;left:35px;width:610px;top:706px;text-align:center;font-weight:700;font-size:20px;line-height:31px;letter-spacing:.3px}
.back-label{position:absolute;left:712px;top:185px;width:455px;height:610px;background:linear-gradient(90deg,var(--purple-dark),var(--purple-light) 50%,var(--purple-dark))}
.back-frame{position:absolute;inset:10px;border:1.5px solid var(--frame)}
.back-text{position:absolute;left:33px;width:390px}
.claim{top:49px;text-align:center;font-family:"Oswald",sans-serif;font-weight:500;font-size:14.5px;line-height:23px;letter-spacing:.3px}
.serving{top:115px;text-align:center;font-family:"Oswald",sans-serif;font-weight:500;font-size:14.5px}
.description{top:159px;font-size:13px;line-height:18px}
.ingredients{top:202px;font-size:13px;line-height:18px}
.ingredients b{font-weight:700}
.nutrition{position:absolute;left:35px;top:250px;width:213px;border:1px solid var(--white);border-collapse:collapse;font-size:12px;line-height:13px}
.nutrition td{padding:1px 4px;vertical-align:top}
.nutrition .head td{border-bottom:1px solid var(--white)}
.nutrition .gap td{padding-top:10px}
.badges{position:absolute;left:268px;top:272px;list-style:none;font-size:10.5px;font-weight:700;line-height:12px}
.badges li{display:flex;align-items:flex-start;gap:9px;height:27px}
.badges svg{flex:none;margin-top:-2px}
.volume{position:absolute;left:28px;top:590px;transform-origin:0 0;transform:rotate(-90deg);font-family:"Oswald",sans-serif;font-weight:600;font-size:36px;line-height:36px;white-space:nowrap}
.deposit{position:absolute;left:84px;top:590px;transform-origin:0 0;transform:rotate(-90deg);font-family:"Oswald",sans-serif;font-weight:500;font-size:11px;white-space:nowrap}
.code-field{position:absolute;left:125px;top:410px;width:208px;height:200px;background:var(--panel)}
</style>
</head>
<body>
<main class="canvas">
  <svg class="front-shape" width="1200" height="900" viewBox="0 0 1200 900">
    <defs>
      <linearGradient id="labelFill" x1="0" x2="1" y1="0" y2="0">
        <stop offset="0" stop-color="#9a1e90"/>
        <stop offset=".5" stop-color="#c732b9"/>
        <stop offset="1" stop-color="#9a1e90"/>
      </linearGradient>
      <radialGradient id="splashFill" cx=".5" cy=".55" r=".5">
        <stop offset="0" stop-color="#eaf6fb"/>
        <stop offset=".55" stop-color="#9fd3e8" stop-opacity=".75"/>
        <stop offset="1" stop-color="#7cc3df" stop-opacity="0"/>
      </radialGradient>
    </defs>
    <path class="front-label" fill="url(#labelFill)" d="M35 190 L85 190 Q130 190 140 150 Q340 40 540 150 Q550 190 595 190 L645 190 L645 795 L35 795 Z"/>
    <path class="front-frame" fill="none" stroke="#cf6cc8" stroke-width="1.5" d="M50 205 L95 205 Q145 205 155 162 Q340 62 525 162 Q535 205 585 205 L630 205 L630 780 L50 780 Z"/>
    <rect x="150" y="338" width="370" height="330" rx="165" fill="url(#splashFill)" role="img" aria-label="Illustration: Wasserspritzer"/>
  </svg>

  <div class="brand-name">Veltrano</div>

  <p class="tagline">ERFRISCHUNGSGETRÄNK<br>AUS AUFGEBRÜHTEM HIBISKUSTEE</p>

  <section class="back-label">
    <div class="back-frame"></div>
    <p class="back-text claim">VELTRANO IST EIN WAHRER KLASSIKER UNTER DEN<br>ERFRISCHUNGSGETRÄNKEN UND EIN ABSOLUTER TOP-DURSTLÖSCHER.</p>
    <p class="back-text serving">SCHMECKT GEKÜHLT AM BESTEN!</p>
    <p class="back-text description">Das Hibiskus Erfrischungsgetränk ist ein koffeinfreies Getränk aus den Blüten der nordafrikanischen Hibiskuspflanze.</p>
    <p class="back-text ingredients"><b>Zutaten:</b> Teeaufguss mit Wasser aus Hibiskusblüten, Zucker, Zitronensaft*, Kohlensäure, *aus Saftkonzentrat</p>

    <table class="nutrition">
      <tr class="head"><td>Nährwerte</td><td>pro 100 ml</td></tr>
      <tr><td>Brennwert<br>Fett<br>davon gesättigte<br>Fettsäuren</td><td>177 kJ / 42 kcal<br>&lt; 0,30<br><br>0 g</td></tr>
      <tr class="gap"><td>Kohlenhydrate<br>davon Zucker<br>Eiweiß<br>Salz</td><td>10 g<br>10 g<br>&lt; 0,50 g<br>0,03 g</td></tr>
    </table>

    <ul class="badges">
      <li><svg width="16" height="14" viewBox="0 0 16 14"><path d="M1 7 L6 12 L15 2" fill="none" stroke="#fff" stroke-width="3" stroke-linecap="round" stroke-linejoin="round"/></svg><span>Glutenfrei</span></li>
      <li><svg width="16" height="14" viewBox="0 0 16 14"><path d="M1 7 L6 12 L15 2" fill="none" stroke="#fff" stroke-width="3" stroke-linecap="round" stroke-linejoin="round"/></svg><span>Ohne künstliche Aromen</span></li>
      <li><svg width="16" height="14" viewBox="0 0 16 14"><path d="M1 7 L6 12 L15 2" fill="none" stroke="#fff" stroke-width="3" stroke-linecap="round" stroke-linejoin="round"/></svg><span>Keine Farbstoffe</span></li>
      <li><svg width="16" height="14" viewBox="0 0 16 14"><path d="M1 7 L6 12 L15 2" fill="none" stroke="#fff" stroke-width="3" stroke-linecap="round" stroke-linejoin="round"/></svg><span>Keine Konservierungs-<br>stoffe</span></li>
    </ul>

    <div class="volume">0,33 L</div>
    <div class="deposit">PFANDFLASCHE</div>
    <div class="code-field"></div>
  </section>
</main>
</body>
</html>
```